Business Stationery
Business card, letter head and compliment slip
Professional
Jake Hollins
Managing Director
Four Larkmead Row
Birmingham
B7 4QN
jake@corvastel.org.uk
corvastel.org.uk
Corvastel is an appointed representative of Pelvarin Ltd which is authorised and regulated by the Market Conduct Tribunal.

```html
<!DOCTYPE html>
<html lang="en">
<head>
<meta charset="utf-8">
<title>Corvastel Business Stationery</title>
<link rel="stylesheet" href="https://fonts.googleapis.com/css2?family=Arimo:wght@400;700&display=swap">
<style>
  :root {
    --backdrop: #4a4a4a;
    --paper: #ffffff;
    --band: #ececec;
    --ink: #000000;
    --brand: #c8231b;
    --shadow: rgba(0,0,0,0.45);
  }
  * { box-sizing: border-box; margin: 0; padding: 0; }
  html, body { width: 1200px; height: 1027px; overflow: hidden; }
  body {
    background: var(--backdrop);
    font-family: "Arimo", Arial, sans-serif;
    color: var(--ink);
    position: relative;
  }
  .sheet {
    position: absolute;
    background: var(--paper);
    box-shadow: 4px 6px 14px var(--shadow);
    overflow: hidden;
  }
  .brand { display: flex; flex-direction: column; align-items: flex-start; }
  .brand-name {
    display: flex; align-items: center; gap: 6px;
    font-weight: 700; color: var(--ink); letter-spacing: -0.5px; line-height: 1;
  }
  .brand-mark { background: var(--brand); display: inline-block; }
  .brand-tagline { font-weight: 400; color: var(--ink); white-space: nowrap; }

  /* Business card front */
  .card-front { left: 39px; top: 50px; width: 340px; height: 184px; font-size: 8px; line-height: 1.35; z-index: 1; }
  .card-front .holder { position: absolute; left: 16px; top: 14px; }
  .card-front .web { position: absolute; right: 16px; top: 14px; text-align: right; }
  .card-front .numbers { position: absolute; left: 16px; top: 124px; display: grid; grid-template-columns: 32px auto; }
  .card-front .postal { position: absolute; right: 16px; top: 124px; text-align: right; }

  /* Business card back */
  .card-back { left: 39px; top: 242px; width: 340px; height: 181px; z-index: 1; }
  .card-back .notice {
    position: absolute; left: 14px; top: 12px; width: 262px; height: 40px;
    background: var(--band); font-size: 7px; line-height: 1.4; padding: 6px 8px;
  }
  .card-back .brand { position: absolute; left: 14px; top: 84px; }
  .card-back .brand-name { font-size: 38px; }
  .card-back .brand-mark { width: 14px; height: 14px; }
  .card-back .brand-tagline { font-size: 13px; margin-top: 2px; }
  .card-back .web { position: absolute; right: 16px; bottom: 10px; font-size: 11px; font-weight: 700; }

  /* Letterhead */
  .letterhead { left: 437px; top: 50px; width: 729px; height: 938px; z-index: 1; }
  .letterhead .header { position: absolute; left: 0; top: 0; width: 100%; height: 123px; background: var(--band); }
  .letterhead .brand { position: absolute; left: 211px; top: 44px; }
  .letterhead .brand-name { font-size: 60px; }
  .letterhead .brand-mark { width: 20px; height: 20px; }
  .letterhead .brand-tagline { font-size: 19px; margin-top: 2px; }
  .letterhead .postal { position: absolute; left: 24px; top: 140px; font-size: 19px; line-height: 1.3; }
  .letterhead .numbers {
    position: absolute; right: 22px; top: 140px; font-size: 19px; line-height: 1.3;
    display: grid; grid-template-columns: 68px auto;
  }
  .letterhead .steps { position: absolute; right: 0; bottom: 36px; width: 114px; height: 103px; }
  .letterhead .footer {
    position: absolute; left: 0; bottom: 0; width: 100%; height: 36px; background: var(--ink);
    color: var(--paper); font-size: 17px; font-weight: 700; text-align: center; line-height: 36px;
  }

  /* Compliment slip, resting on top of the letterhead */
  .slip { left: 39px; top: 451px; width: 824px; height: 362px; z-index: 2; }
  .slip .header { position: absolute; left: 0; top: 0; width: 225px; height: 84px; background: var(--band); }
  .slip .brand { position: absolute; left: 22px; top: 28px; }
  .slip .brand-name { font-size: 34px; }
  .slip .brand-mark { width: 12px; height: 12px; }
  .slip .brand-tagline { font-size: 10px; margin-top: 1px; }
  .slip .postal { position: absolute; left: 24px; top: 94px; font-size: 8px; }
  .slip .steps { position: absolute; right: 0; bottom: 0; width: 100px; height: 84px; }
</style>
</head>
<body>

  <section class="sheet card-front" aria-label="Business card front">
    <div class="holder">Jake Hollins<br>Managing Director</div>
    <div class="web">jake@corvastel.org.uk<br>www.corvastel.org.uk</div>
    <div class="numbers">
      <span>Phone:</span><span>0121 496 0732</span>
      <span>Cell:</span><span>07700 900418</span>
      <span>Fax:</span><span>0121 496 0815</span>
    </div>
    <div class="postal">Four Larkmead Row<br>Birmingham<br>B7 4QN</div>
  </section>

  <section class="sheet card-back" aria-label="Business card back">
    <p class="notice">Corvastel is an appointed representative of Pelvarin Ltd which is authorised and regulated by the Market Conduct Tribunal.</p>
    <div class="brand">
      <span class="brand-name">corvastel <span class="brand-mark"></span></span>
      <span class="brand-tagline">Independent financial advice for Doctors</span>
    </div>
    <p class="web">www.corvastel.org.uk</p>
  </section>

  <section class="sheet letterhead" aria-label="Letterhead">
    <div class="header"></div>
    <div class="brand">
      <span class="brand-name">corvastel <span class="brand-mark"></span></span>
      <span class="brand-tagline">Independent financial advice for Doctors</span>
    </div>
    <div class="postal">Four Larkmead Row<br>Birmingham<br>B7 4QN</div>
    <div class="numbers">
      <span>Phone:</span><span>0121 496 0732</span>
      <span>Cell:</span><span>07700 900418</span>
      <span>Fax:</span><span>0121 496 0815</span>
    </div>
    <svg class="steps" viewBox="0 0 114 103" aria-hidden="true">
      <polygon points="0,103 0,77 28,77 28,51 57,51 57,26 85,26 85,0 114,0 114,103" fill="#000"/>
    </svg>
    <footer class="footer">www.corvastel.org.uk</footer>
  </section>

  <section class="sheet slip" aria-label="Compliment slip">
    <div class="header"></div>
    <div class="brand">
      <span class="brand-name">corvastel <span class="brand-mark"></span></span>
      <span class="brand-tagline">Independent financial advice for Doctors</span>
    </div>
    <p class="postal">Four Larkmead Row, Birmingham, B7 4QN</p>
    <svg class="steps" viewBox="0 0 100 84" aria-hidden="true">
      <polygon points="0,84 0,56 33,56 33,28 66,28 66,0 100,0 100,84" fill="#000"/>
    </svg>
  </section>

</body>
</html>
```